Press Upon Ink needs a New Website Design

Press Upon Ink is a small rubber stamp & scrapbook company operating in the arts & crafts space. We currently own 6 company brands plus Press Upon Ink which is the main business & website, www.pressuponink.net.
We are launching a new eCommerce store to bring all the companies under one shopping platform instead of the 6 there are currently. We need a new site design that incorporates the shop by brand idea making it super easy to navigate and understand. Brand logos should be displayed on all pages in header design similar to http://www.tidewove.com and https://bazaar.quellmark.com
The brand logo for Bravado! Stamps is currently being designed so that one is missing from the brief.
Top menu: Home, Shop, Videos, Gallery, Blogs, Show Schedule, PUI Brands or Brands
Utilize “Welcome to PressUponInk” tagline in design
Include “Art Rubber Stamps and Scrapbooking Supplies” tagline on at least home page
Need 3 pages designed, must be designed with responsive in mind.
Home page
Product Listing page
Product Detail page
Colors
Browns - use colors from background image attached
#981E1E
# 3B2313
Competitors
http://craftlostfree.com
https://inkersunnamed.com
http://www.morvelsllc.com
http://www.lubrofcraft.com
http://www.quvprints.com
http://www.thistlebrand.us
The shopping cart system being used is Cartwell (http://demo.cartwell.com/) if you are familiar with creating html templates for Cartwell there is additional opportunity to convert the design into html/css
Target Market(s)
Handmade Cardmakers, Scrapbookers, Papercrafters

```html
<!DOCTYPE html>
<html lang="en">
<head>
<meta charset="utf-8">
<title>Press Upon Ink – Art Rubber Stamps and Scrapbooking Supplies</title>
<link href="https://fonts.googleapis.com/css2?family=Open+Sans:wght@400;600;700;800&display=swap" rel="stylesheet">
<style>
:root{
  --red:#981E1E;
  --red-dark:#7f1818;
  --brown:#3B2313;
  --brown-mid:#4a2c18;
  --ink:#222;
  --muted:#666;
  --line:#ddd;
  --stage:#ece8e4;
  --white:#fff;
}
*{box-sizing:border-box;margin:0;padding:0}
html,body{width:681px;height:1200px;overflow:hidden}
body{background:var(--stage);font-family:"Open Sans",sans-serif;color:var(--ink);position:relative}
a{color:inherit;text-decoration:none}
.page{position:absolute;left:76px;top:0;width:530px;height:1200px;background:var(--white);overflow:hidden}
.abs{position:absolute}

.brand-strip{left:0;top:0;width:530px;height:46px;display:flex;align-items:center;justify-content:space-between;padding:0 6px;border-bottom:1px solid var(--line)}
.brand-strip span{font-size:8.5px;font-weight:700;color:var(--brown);white-space:nowrap}
.brand-strip .brand-box{height:32px;display:flex;align-items:center;padding:0 6px;background:#8ea9c0;color:var(--white)}

.logo{left:12px;top:52px;width:92px;height:90px;display:flex;flex-direction:column;align-items:center;justify-content:center;gap:4px}
.logo i{width:26px;height:26px;border-radius:50%;background:var(--brown);display:block}
.logo b{font-size:13px;font-weight:800;color:var(--brown);text-align:center;line-height:1.1}
.account-bar{left:306px;top:46px;width:224px;height:24px;background:var(--brown);display:flex;justify-content:space-around;align-items:center;clip-path:polygon(8px 0,100% 0,100% 100%,0 100%)}
.account-bar a{font-size:5.6px;color:var(--white);padding-left:4px}
.search{left:305px;top:78px;width:123px;height:27px;border:1px solid #ccc;display:flex;align-items:center;gap:7px;padding-left:8px;font-size:5.5px;color:#888}
.cart{left:436px;top:78px;width:84px;height:27px;border:1.5px solid var(--red);display:flex;align-items:center;gap:5px;padding-left:7px;font-size:5.5px;color:var(--ink)}
.cart strong{color:var(--red);font-size:8px}
.cart .badge{position:absolute;left:14px;top:3px;width:9px;height:9px;border-radius:50%;background:var(--red);color:var(--white);font-size:5px;display:flex;align-items:center;justify-content:center}
.main-nav{left:115px;top:115px;width:407px;height:25px;background:var(--red);display:flex;border-radius:3px 0 0 0}
.main-nav a{font-size:7px;color:var(--white);padding:0 10px;display:flex;align-items:center;border-right:1px solid rgba(255,255,255,.25)}
.main-nav a.active{background:var(--brown);border-radius:3px 0 0 0}

.sidebar{left:6px;top:146px;width:116px;height:199px;background:var(--brown);padding:13px 10px 0}
.sidebar h2{font-size:10.5px;font-weight:800;color:var(--white);margin-bottom:6px}
.sidebar li{list-style:none;font-size:6px;color:#eee;height:19px;display:flex;align-items:center;border-bottom:1px solid rgba(255,255,255,.12)}
.sidebar li::before{content:"›";margin:0 6px 0 2px}
.slider{left:122px;top:146px;width:400px;height:199px;background:linear-gradient(120deg,#c9b9a6,#b98478 35%,#8a8f74 60%,#a8adaf 85%,#d2a9a0)}
.slider-caption{left:122px;top:262px;width:400px;text-align:center;color:var(--white)}
.slider-caption p{font-size:8.5px;font-weight:600}
.slider-caption h1{font-size:12.5px;font-weight:700;margin-top:1px}
.dots{left:288px;top:320px;display:flex;gap:7px}
.dots i{width:5px;height:5px;border-radius:50%;background:var(--white);display:block}
.dots i.on{background:none;border:1px solid var(--white)}

.section-title{font-size:12.5px;font-weight:800;color:var(--red);letter-spacing:.2px}
.arrows{left:494px;top:360px;display:flex;gap:2px}
.arrows span{width:13px;height:13px;background:#bbb;color:var(--white);font-size:9px;display:flex;align-items:center;justify-content:center}

.card{top:382px;width:122px;height:178px;border:1px solid var(--line);text-align:center}
.card .thumb{width:94px;height:94px;margin:12px auto 0}
.card h3{font-size:6.5px;font-weight:600;margin-top:12px}
.card .price{font-size:10px;font-weight:700;color:var(--red);margin-top:3px}
.card .btn{display:inline-block;margin-top:4px;background:var(--red);color:var(--white);font-size:5.5px;font-weight:700;padding:4px 8px}

.video{left:10px;top:602px;width:277px;height:220px;background:linear-gradient(180deg,#7c7a7b,#6e4e4e 45%,#3a3535)}
.play{left:111px;top:678px;width:58px;height:58px}
.video-caption{left:20px;top:790px;color:var(--white)}
.video-caption h3{font-size:8.5px;font-weight:700}
.video-caption p{font-size:6.5px}

.post{left:300px;width:222px;height:70px}
.post .pic{position:absolute;left:0;top:0;width:85px;height:62px}
.post .body{position:absolute;left:97px;top:2px;width:128px}
.post time{font-size:5px;font-style:italic;color:var(--muted)}
.post h3{font-size:6.6px;font-weight:600;margin:3px 0 5px}
.post p{font-size:5.3px;color:var(--muted);line-height:1.55}
.post .more{font-size:5.5px;font-weight:700;color:var(--red);margin-top:7px;display:block}

.coupon{left:11px;top:842px;width:278px;height:149px;background:linear-gradient(135deg,#6d5448,#5a4036 50%,#6f5a52);text-align:center;color:var(--white);padding-top:30px}
.coupon h2{font-size:19px;font-weight:400}
.coupon h2 b{font-weight:800}
.coupon p{font-size:6.5px;line-height:1.5;margin-top:4px;color:#eee}
.coupon .btn{display:inline-block;margin-top:14px;border:1px solid var(--white);background:var(--red);font-size:6px;font-weight:700;padding:8px 10px}
.newsletter{left:289px;top:842px;width:228px;height:149px;background:var(--red);text-align:center;color:var(--white);padding-top:20px}
.newsletter h2{font-size:13px;font-weight:400;line-height:1}
.newsletter h2 b{display:block;font-size:19px;font-weight:800;margin-top:3px}
.email{position:absolute;left:25px;top:80px;width:180px;height:34px;border:1.5px solid #d86060;display:flex;align-items:center}
.email span{flex:1;text-align:left;padding-left:10px;font-size:6.5px;display:flex;gap:9px;align-items:center}
.email .go{width:40px;height:100%;border-left:1.5px solid #d86060;display:flex;align-items:center;justify-content:center}

.footer{left:0;top:1008px;width:530px;height:192px;background:var(--red);color:var(--white)}
.footer-logo{position:absolute;left:28px;top:22px;width:70px;height:80px;display:flex;flex-direction:column;align-items:center;justify-content:center;gap:5px}
.footer-logo i{width:24px;height:24px;border-radius:50%;background:var(--white);display:block}
.footer-logo b{font-size:11px;font-weight:800;text-align:center;line-height:1.1}
.fcol{position:absolute;top:28px}
.fcol h4{font-size:6.8px;font-weight:700;margin-bottom:6px}
.fcol li{list-style:none;font-size:5.5px;line-height:9px}
.fcol.social li{display:flex;gap:6px;align-items:center;line-height:13.5px}
.copy{position:absolute;left:0;width:530px;top:174px;text-align:center;font-size:5px}
</style>
</head>
<body>
<div class="page">

  <div class="abs brand-strip">
    <span class="brand-box">Gleaming Prints</span>
    <span style="color:var(--red)">Crafted</span>
    <span>Hopeful Imprints</span>
    <span>RM Sparkle</span>
    <span style="color:#2e6b2e">ZVL Roundup</span>
  </div>

  <div class="abs logo"><i></i><b>Press Upon<br>Ink</b></div>

  <nav class="abs account-bar">
    <a href="#">My Account</a><a href="#">My Wishlist</a><a href="#">Checkout</a><a href="#">Login</a>
  </nav>

  <div class="abs search">
    <svg width="7" height="7" viewBox="0 0 10 10"><circle cx="4" cy="4" r="3" fill="none" stroke="#888" stroke-width="1.3"/><path d="M6.3 6.3L9 9" stroke="#888" stroke-width="1.3"/></svg>SEARCH
  </div>

  <div class="abs cart">
    <svg width="14" height="12" viewBox="0 0 14 12"><path d="M0 1h2.5l2 7h7l1.5-5H4" fill="none" stroke="#333" stroke-width="1.4"/><circle cx="5.5" cy="10.5" r="1.2" fill="#333"/><circle cx="10.5" cy="10.5" r="1.2" fill="#333"/></svg>
    <span class="badge">0</span>MY CART <strong>$0.00</strong>
  </div>

  <nav class="abs main-nav">
    <a href="#" class="active">Home</a><a href="#">Shop</a><a href="#">Videos</a><a href="#">Gallery</a><a href="#">Blogs</a><a href="#">Show Schedule</a><a href="#">PUI Brands</a><a href="#" style="border:0">Contact us</a>
  </nav>

  <aside class="abs sidebar">
    <h2>PRODUCTS</h2>
    <ul>
      <li>Adhesives</li><li>Accessories</li><li>Outline Stickers(by MiMi)</li><li>Edge-Ups</li><li>RM Sparkle Products</li><li>Art Acetates</li><li>Crafted Stamper Stamp Line</li><li style="border:0">Dbl. Embossed Stickers</li>
    </ul>
  </aside>

  <div class="abs slider" role="img" aria-label="Collage of stamped artwork: flowers, a winged insect, roses, a window scene and a craft kit"></div>
  <div class="abs slider-caption"><p>Welcome to PressUponInk</p><h1>Art Rubber Stamps and Scrapbooking Supplies</h1></div>
  <div class="abs dots"><i></i><i class="on"></i><i></i><i></i><i></i></div>

  <h2 class="abs section-title" style="left:8px;top:358px">PRODUCTS</h2>
  <div class="abs arrows"><span>‹</span><span>›</span></div>

  <div class="abs card" style="left:9px">
    <div class="thumb" role="img" aria-label="Black and white moth stamp print" style="background:radial-gradient(circle,#777,#ddd 70%,#fff)"></div>
    <h3>Moth Formal, Art Prime</h3><div class="price">$4.95</div><a class="btn" href="#">ADD TO CART</a>
  </div>
  <div class="abs card" style="left:140px">
    <div class="thumb" role="img" aria-label="Four aged-tone succulent prints" style="background:linear-gradient(135deg,#e8eee0,#b9c9a4 50%,#e6c8bd)"></div>
    <h3>Succulents 2, Aged Tone</h3><div class="price">$4.95</div><a class="btn" href="#">ADD TO CART</a>
  </div>
  <div class="abs card" style="left:271px">
    <div class="thumb" role="img" aria-label="Adobe window stamped scene" style="background:linear-gradient(180deg,#d8958a,#c6897a 60%,#8f9a88)"></div>
    <h3>Adobe Window</h3><div class="price">$4.95</div><a class="btn" href="#">ADD TO CART</a>
  </div>
  <div class="abs card" style="left:400px">
    <div class="thumb" role="img" aria-label="Complete craft kit in clear packaging" style="background:linear-gradient(160deg,#d9d9dd,#b2b2b8 60%,#cfcfd4)"></div>
    <h3>RM Sparkle COMPLETE Kit</h3><div class="price">$4.95</div><a class="btn" href="#">ADD TO CART</a>
  </div>

  <h2 class="abs section-title" style="left:9px;top:578px">VIDEOS</h2>
  <h2 class="abs section-title" style="left:300px;top:578px">BLOG</h2>

  <div class="abs video" role="img" aria-label="Video still of the store's trade show booth with banner"></div>
  <svg class="abs play" viewBox="0 0 58 58"><circle cx="29" cy="29" r="26" fill="none" stroke="#fff" stroke-width="5"/><path d="M22 16l20 13-20 13z" fill="#fff"/></svg>
  <div class="abs video-caption"><h3>At vero eos et accusamus et</h3><p>On the other hand</p></div>

  <article class="abs post" style="top:602px">
    <div class="pic" role="img" aria-label="Craft kits on a table" style="background:linear-gradient(135deg,#c7c5cc,#a9a6ae)"></div>
    <div class="body"><time>02 May, 2016</time><h3>SED UT PERSPICIATIS UNDE OMNIS</h3><p>But I must explain to you how all this mistaken idea of denouncing</p><a class="more" href="#">READ MORE ›</a></div>
  </article>
  <article class="abs post" style="top:681px">
    <div class="pic" role="img" aria-label="Stamped reed artwork on rust card" style="background:linear-gradient(135deg,#b5502f,#8a3a22)"></div>
    <div class="body"><time>02 May, 2016</time><h3>AT VERO EOS ET ACCUSAMUS</h3><p>On the other hand, we denounce with righteous indignation.</p><a class="more" href="#">READ MORE ›</a></div>
  </article>
  <article class="abs post" style="top:760px">
    <div class="pic" role="img" aria-label="Stamped cattail pond artwork" style="background:linear-gradient(135deg,#c7a772,#9a8450)"></div>
    <div class="body"><time>02 May, 2016</time><h3>BUT I MUST EXPLAIN TO YOU</h3><p>pleasure that has no annoying consequences, or one who avoids a pain</p><a class="more" href="#">READ MORE ›</a></div>
  </article>

  <section class="abs coupon" role="img" aria-label="Vintage acetate print samples behind a dark overlay">
    <h2>GET <b>10%</b> OFF</h2>
    <p>Our Art Acetates are high quality prints<br>on heatable, embossable.</p>
    <a class="btn" href="#">USE COUPON CODE</a>
  </section>

  <section class="abs newsletter">
    <h2>NEWSLETTER<b>SUBSCRIBE</b></h2>
    <div class="email">
      <span><svg width="8" height="6" viewBox="0 0 8 6"><rect x=".5" y=".5" width="7" height="5" fill="none" stroke="#fff"/><path d="M.5.5L4 3.5 7.5.5" fill="none" stroke="#fff"/></svg>E mail id</span>
      <div class="go"><svg width="20" height="10" viewBox="0 0 20 10"><path d="M0 5h18M13 1l5 4-5 4" fill="none" stroke="#fff" stroke-width="2"/></svg></div>
    </div>
  </section>

  <footer class="abs footer">
    <div class="footer-logo"><i></i><b>Press Upon<br>Ink</b></div>
    <div class="fcol" style="left:161px"><h4>CONTACT US</h4><ul><li>Home</li><li>Shop</li><li>Videos</li><li>Gallery</li><li>Blogs</li><li>Show Schedule</li><li>PUI Brands</li><li>Contact us</li></ul></div>
    <div class="fcol" style="left:267px"><h4>MENU</h4><ul><li>Home</li><li>Shop</li><li>Videos</li><li>Gallery</li><li>Blogs</li><li>Show Schedule</li><li>PUI Brands</li><li>Contact us</li></ul></div>
    <div class="fcol" style="left:357px"><h4>LINKS</h4><ul><li>My Account</li><li>View Cart</li><li>Go to Checkout</li><li>Gallery Categories</li></ul></div>
    <div class="fcol social" style="left:448px"><h4>FOLLOW US ON</h4><ul>
      <li><svg width="5" height="5"><rect width="5" height="5" fill="#fff"/></svg>Friendbook</li>
      <li><svg width="5" height="5"><rect width="5" height="5" fill="#fff"/></svg>Chirper</li>
      <li><svg width="5" height="5"><rect width="5" height="5" fill="#fff"/></svg>Workednet</li>
      <li><svg width="5" height="5"><circle cx="2.5" cy="2.5" r="2.5" fill="#fff"/></svg>RSS Feed</li>
    </ul></div>
    <p class="copy">Copyrihgts @ 2016 All Rights Reserved</p>
  </footer>

</div>
</body>
</html>
```